Bouncy castle rental needs a car wrap design

We are a young startup that rents out bouncy castles. We live in Crailsheim and have the following vehicles:
- Vornik Astra Q 2024 in white
- Car trailer
We have already had logo files created through a competition. These files are all attached.
Our website: https://fantorix-welbach.de
We would like a partial foiling, with the logo and other elements from the logo files adapted - feel free to be creative! :-) You can/may also use images from the homepage, for example. However, we are not sure how bouncy castles should be depicted on the car...
The design should be striking, young, lively and convey the theme of bouncy castles :-)
You will receive the following information as files:
- Zip file with some logo design files
- a photo of the Vornik Astra Q 2024
- A photo of the car trailer. Here are the dimensions:
- Side: 250cm x 153cm
- Front/back: 150cm x153cm
#Additional Information:
Colors frequently used on website:
Yellow: #fbd604
Yellow: #d41370
Also added our logo with white border, that it can be used on color and not just white

```html
<!DOCTYPE html>
<html lang="de">
<head>
<meta charset="utf-8">
<title>Fantorix Welbach – Anhänger-Beschriftung</title>
<link rel="stylesheet" href="https://fonts.googleapis.com/css2?family=Gochi+Hand&family=Roboto+Condensed:wght@700&display=swap">
<style>
  :root {
    --yellow: #f2c80f;
    --yellow-light: #f9de5a;
    --ink: #222226;
    --panel-white: #f1f1f1;
    --blue: #3a9fd8;
    --green: #7cc142;
    --icon-gold: #e0b43c;
    --icon-blue: #4a9cd6;
    --icon-green: #5fb44a;
    --icon-red: #d83a3a;
    --page: #ffffff;
  }
  html, body {
    margin: 0;
    padding: 0;
    width: 883px;
    height: 1200px;
    overflow: hidden;
    background: var(--page);
  }
  .canvas {
    position: relative;
    width: 883px;
    height: 1200px;
  }
  .panel {
    position: absolute;
    overflow: hidden;
    box-shadow: 0 0 0 1px #d8d8d8;
  }

  /* Side panel 250 x 153 */
  .side-panel {
    left: 41px;
    top: 60px;
    width: 800px;
    height: 490px;
    background: var(--panel-white);
  }
  .side-header {
    position: absolute;
    left: 0; top: 0;
    width: 800px;
    height: 150px;
  }
  .side-title {
    position: absolute;
    left: 0; top: 22px;
    width: 800px;
    margin: 0;
    text-align: center;
    font-family: "Gochi Hand", cursive;
    font-size: 64px;
    letter-spacing: 2px;
    color: var(--ink);
    text-transform: uppercase;
    line-height: 1;
    white-space: nowrap;
  }
  .scene-art {
    position: absolute;
    left: 390px;
    top: 130px;
    width: 410px;
    height: 300px;
    background: linear-gradient(180deg, rgba(210,215,220,0.6) 0%, rgba(242,200,15,0.85) 55%, #2b2b2b 100%);
    border-top-left-radius: 180px 120px;
  }
  .contact-list {
    position: absolute;
    left: 36px;
    top: 150px;
    margin: 0;
    padding: 0;
    list-style: none;
    font-family: "Roboto Condensed", sans-serif;
    font-weight: 700;
    font-size: 25px;
    color: var(--ink);
    letter-spacing: 1px;
  }
  .contact-item {
    display: flex;
    align-items: center;
    height: 54px;
    white-space: nowrap;
  }
  .contact-item .icon {
    width: 28px;
    height: 28px;
    margin-right: 14px;
    flex: none;
  }
  .contact-item.continued { padding-left: 42px; height: 40px; }
  .side-footer {
    position: absolute;
    left: 0; bottom: 0;
    width: 800px;
    height: 70px;
    background: var(--yellow);
  }
  .owner-name {
    position: absolute;
    left: 28px; bottom: 8px;
    margin: 0;
    font-family: "Gochi Hand", cursive;
    font-size: 50px;
    letter-spacing: 2px;
    text-transform: uppercase;
    line-height: 1;
    white-space: nowrap;
  }
  .owner-name .first { color: var(--blue); }
  .owner-name .last { color: var(--green); }

  /* Front panel 150 x 153 */
  .front-panel {
    left: 201px;
    top: 620px;
    width: 480px;
    height: 490px;
  }
  .sunburst {
    position: absolute;
    inset: 0;
    background: radial-gradient(circle at 50% 55%, var(--yellow-light) 0%, var(--yellow) 70%);
  }
  .front-name {
    position: absolute;
    left: 0; top: 56px;
    width: 100%;
    margin: 0;
    text-align: center;
    font-family: "Gochi Hand", cursive;
    font-size: 40px;
    letter-spacing: 2px;
    text-transform: uppercase;
    line-height: 1;
    white-space: nowrap;
  }
  .front-name .first { color: var(--blue); }
  .front-name .last { color: var(--green); }
  .brand-mark {
    position: absolute;
    left: 0; top: 245px;
    width: 100%;
    display: flex;
    align-items: center;
    justify-content: center;
    gap: 12px;
  }
  .brand-mark .dot {
    width: 28px;
    height: 28px;
    border-radius: 50%;
    background: var(--ink);
    flex: none;
  }
  .brand-mark .brand-name {
    font-family: "Gochi Hand", cursive;
    font-size: 36px;
    color: var(--ink);
    text-transform: uppercase;
    letter-spacing: 1px;
    line-height: 1;
    white-space: nowrap;
  }
</style>
</head>
<body>
<main class="canvas">

  <section class="panel side-panel" aria-label="Seitenwand">
    <svg class="side-header" viewBox="0 0 800 150" aria-hidden="true">
      <path d="M0 0 H800 V92 H330 C300 92 250 150 180 128 C120 110 70 92 0 92 Z" fill="var(--yellow)"/>
    </svg>
    <h1 class="side-title">Fantorix Welbach</h1>

    <div class="scene-art" role="img" aria-label="Illustration: Hüpfburg vor einer Stadtsilhouette"></div>

    <ul class="contact-list">
      <li class="contact-item">
        <svg class="icon" viewBox="0 0 28 28" aria-hidden="true">
          <circle cx="14" cy="14" r="13" fill="#fff" stroke="var(--icon-gold)" stroke-width="2"/>
          <circle cx="14" cy="14" r="7" fill="none" stroke="var(--icon-gold)" stroke-width="1.5"/>
          <ellipse cx="14" cy="14" rx="3" ry="7" fill="none" stroke="var(--icon-gold)" stroke-width="1.5"/>
          <line x1="7" y1="14" x2="21" y2="14" stroke="var(--icon-gold)" stroke-width="1.5"/>
        </svg>
        www.fantorix-welbach.de
      </li>
      <li class="contact-item">
        <svg class="icon" viewBox="0 0 28 28" aria-hidden="true">
          <circle cx="14" cy="14" r="13" fill="#fff" stroke="var(--icon-blue)" stroke-width="2"/>
          <rect x="7" y="9" width="14" height="10" fill="var(--icon-blue)"/>
          <path d="M7 9 L14 15 L21 9" fill="none" stroke="#fff" stroke-width="1.5"/>
        </svg>
        info@fantorix-welbach.de
      </li>
      <li class="contact-item">
        <svg class="icon" viewBox="0 0 28 28" aria-hidden="true">
          <circle cx="14" cy="14" r="13" fill="#fff" stroke="var(--icon-green)" stroke-width="2"/>
          <path d="M9 7 L12 7 L13 11 L11 12.5 C12 15 13 16 15.5 17 L17 15 L21 16 L21 19 C21 20 20 21 19 21 C12 21 7 16 7 9 C7 8 8 7 9 7 Z" fill="var(--icon-green)"/>
        </svg>
        0170 / 555 0192
      </li>
      <li class="contact-item">
        <svg class="icon" viewBox="0 0 28 28" aria-hidden="true">
          <circle cx="14" cy="14" r="13" fill="#fff" stroke="var(--icon-red)" stroke-width="2"/>
          <path d="M14 22 C10 17 9 14 9 12 A5 5 0 0 1 19 12 C19 14 18 17 14 22 Z" fill="var(--icon-red)"/>
          <circle cx="14" cy="12" r="2" fill="#fff"/>
        </svg>
        Lindenweg 14
      </li>
      <li class="contact-item continued">74999 Welbach</li>
    </ul>

    <div class="side-footer">
      <p class="owner-name"><span class="first">Lennart</span> <span class="last">Voss</span></p>
    </div>
  </section>

  <section class="panel front-panel" aria-label="Stirnseite">
    <div class="sunburst" role="img" aria-label="Gelbes Strahlenmuster als Hintergrund"></div>
    <p class="front-name"><span class="first">Lennart</span> <span class="last">Voss</span></p>
    <div class="brand-mark">
      <span class="dot" aria-hidden="true"></span>
      <span class="brand-name">Fantorix Welbach</span>
    </div>
  </section>

</main>
</body>
</html>
```